self-employed education content specialist/consultant needs business card and logo design

I need a design for a double-sided business card (and logo) for my nascent consultancy business based in London UK, to hand out at a London trade show in a couple of weeks. The business simply has my name, "Marcus Tenwold".

I describe my service as a "content and engagement consultant". In essence I cover 2 areas:
- Advice to organisations on effective strategies and tactics for creating and distributing large volumes of media-rich content (video and interactive) for learning, training and professional development, that successfully engages and impacts on students and their teachers.
- Advice on growing and maintaining customer/end-user engagement to help maximise the reach and usage of this content.

I have uploaded a weighted list of key words that offer I hope a good feel of "the brand".

In terms of design I have put together a very rough initial idea for the card (see attached doc), which gives an idea of the key messages in text, but I feel it is not working visually, and looks too amateur. In particular I think the background/visuals of the info side needs work; the word cloud on the back of the card is perhaps rather "passé" and could be improved on; there is no "logo" at present; and I think overall it's not very "creative", i.e. it doesn't "stand out".

I am not set on font or background colours/design. The font itself should not be too businessy or too "comic sans", hence I've currently gone for something like Odile or Playfair Display.

Also note that
1. given budget and time constraints, I'm looking for designs for printing on paper, and to be of a fairly standard business card shape/size.
2. I have no web address at present, but will need a card design that can cope with this being added at a later date.

Overall I am hoping for something fairly clean, simple and clear, that will impress and speak to senior managers/business owners working in the education and edtech sectors.

As a self-employed consultant my budget is limited, so I don't expect the world for what I can offer, but am hoping that there are design experts out there who can swiftly interpret my brief and produce something suitable for my needs.

Target Market(s)

senior managers/business owners working in the education and edtech sectors.

Contact Information for Business Card

marcus tenwold
content and engagement consultant
education - training - development
+44 (0) 7731 482905
marcus.tenwold@quorvane.com

Font styles to use
Other font styles liked:
• Odile or Playfair Display are my favourites for now.

Colors

Designer to choose colors to be used in the design.

```html
<!DOCTYPE html>
<html lang="en">
<head>
<meta charset="utf-8">
<title>Marcus Tenwold — Business Card</title>
<link rel="stylesheet" href="https://fonts.googleapis.com/css2?family=Playfair+Display:wght@400;700&family=Montserrat:wght@300;500&display=swap">
<style>
  :root {
    --page: #2a2c30;
    --card: #050505;
    --ink-soft: #d9d9d9;
    --ink-white: #ffffff;
    --accent-orange: #f39a21;
    --accent-green: #6fd11c;
  }
  * { box-sizing: border-box; margin: 0; padding: 0; }
  html, body {
    width: 1200px; height: 900px; overflow: hidden;
    background: var(--page);
  }
  .sheet {
    width: 1200px; height: 900px;
    display: flex; flex-direction: column;
    align-items: center; justify-content: center;
    gap: 40px;
  }
  .card {
    position: relative;
    width: 700px; height: 400px;
    background: var(--card);
    border-radius: 30px;
    overflow: hidden;
    box-shadow: 0 10px 30px rgba(0,0,0,.45);
  }

  /* Front */
  .card-front .identity {
    position: absolute; left: 160px; top: 52px;
  }
  .card-front .name {
    font-family: "Playfair Display", serif;
    font-weight: 400; font-size: 30px;
    letter-spacing: 4px; text-transform: uppercase;
    color: var(--ink-soft);
  }
  .card-front .role {
    margin-top: 4px;
    font-family: "Montserrat", sans-serif;
    font-weight: 500; font-size: 10.5px;
    letter-spacing: 1.6px; text-transform: uppercase;
    color: var(--ink-soft);
  }
  .service-band {
    position: absolute; left: 0; right: 0; top: 138px; height: 62px;
    background: var(--accent-orange);
    display: flex; align-items: center;
    padding-left: 56px;
    font-family: "Playfair Display", serif;
    font-weight: 700; font-size: 24px;
    letter-spacing: 4px; text-transform: uppercase;
    color: var(--ink-white);
  }
  .contact-list {
    position: absolute; left: 62px; top: 236px;
    list-style: none;
    font-family: "Montserrat", sans-serif;
    font-weight: 300; font-size: 18px;
    letter-spacing: 2px;
    color: var(--ink-soft);
  }
  .contact-list li {
    display: flex; align-items: center; gap: 14px;
    margin-bottom: 18px;
  }
  .contact-list svg { width: 20px; height: 20px; flex: none; }

  /* Back */
  .card-back .signature-line {
    position: absolute; left: 0; right: 0; top: 150px;
    display: flex; align-items: center; gap: 28px;
  }
  .card-back .rule {
    height: 12px; background: var(--ink-white);
  }
  .card-back .rule-lead { width: 80px; }
  .card-back .rule-tail { flex: 1; }
  .card-back .name {
    font-family: "Playfair Display", serif;
    font-weight: 400; font-size: 46px;
    letter-spacing: 7px; text-transform: uppercase;
    color: var(--accent-green);
    white-space: nowrap;
  }
</style>
</head>
<body>
<main class="sheet">

  <section class="card card-front" aria-label="Business card front">
    <div class="identity">
      <h1 class="name">Marcus Tenwold</h1>
      <p class="role">Content and engagement consultant</p>
    </div>
    <div class="service-band">Education - Training - Development</div>
    <ul class="contact-list">
      <li>
        <svg viewBox="0 0 24 24" aria-hidden="true"><path fill="#d9d9d9" d="M6.6 10.8c1.4 2.8 3.8 5.1 6.6 6.6l2.2-2.2c.3-.3.7-.4 1-.2 1.1.4 2.3.6 3.6.6.6 0 1 .4 1 1V20c0 .6-.4 1-1 1C10.6 21 3 13.4 3 4c0-.6.4-1 1-1h3.5c.6 0 1 .4 1 1 0 1.3.2 2.5.6 3.6.1.3 0 .7-.2 1l-2.3 2.2z"/></svg>
        <span>+44 (0) 7731 482905</span>
      </li>
      <li>
        <svg viewBox="0 0 24 24" aria-hidden="true"><rect x="2" y="5" width="20" height="14" fill="#d9d9d9"/><path d="M2 5l10 8 10-8M2 19l7-7M22 19l-7-7" fill="none" stroke="#050505" stroke-width="1.6"/></svg>
        <span>marcus.tenwold@quorvane.com</span>
      </li>
    </ul>
  </section>

  <section class="card card-back" aria-label="Business card back">
    <div class="signature-line">
      <span class="rule rule-lead"></span>
      <h2 class="name">Marcus Tenwold</h2>
      <span class="rule rule-tail"></span>
    </div>
  </section>

</main>
</body>
</html>
```